THE LANTERN is a mystical scythian creature, which guarded a golden treasure.

i am a published author back in he 1970's...quillford, edgar penhallow, thistlecombe vane. my agent died and the companies have been bought.
i want to publish on my own and have 3 completed novels. ASH LANTERN is the first. i need a book cover, spine and back cover design for the book.
i will use the book design as an important part of a website i am planning for this and the other 2 books. i will need a design for the other books once this is completed.

this book is a thriller; the second is a historical novel, the third is a comedy. i don't know, because of the differing contents whether there should be an consistency in the design. i think not.

i have an excellent Orvell review and will want phrases from it prominently on the design. i like to be involved in the process. although the thriller deals with the Nazis, i don't want a bunch of s.s. officers. I see the book as a labyrinth with almost unbearable twists and turns. it is not a person book, but driven by the PLOT.

the design must be setup for PressLoft ( vendora ) for printing. Font is important.i like black, but not critical.

the Orvell review (below) has an excellent outline and telling of the book.

as the other 2 novels are completed and i need help with a website, this could be more than just one project.

Back Cover Details:
i would like a small photo and 2 line bio next to the photo.on back cover if it fits.... leaving room for the IBSN /barcode.
the cover, design and excerpts are critical for success and i am willing to work and pay extra to have it the best.
i have never done this before as my first 2 novels were published by traditional houses, so, you must forgive any awkwardness in the process.
thank you
+++++++

THIS IS THE ORVELL REVIEW OF THE BOOK::::::::::
ASH LANTERN (THE LANTERN)
Waldecott, Leonard
Manuscript
BOOK REVIEW
Waldecot (A Choir of Tinkers, 1983, etc.) offers an animated chase through Boston and Europe as his characters unravel
a mystery involving six pairs of identical Jewish twins saved from a German concentration camp.
In 1965, Simon Kettering, a scientist fruitlessly searching for the secret of telepathy, receives a tantalizing report of
macabre experiments conducted by Oskar Veltmann, a Nazi researcher on a similar mission. Kettering searches for the
twins who were the subjects of Veltmann’s experiments, and he gets help from Greta Sauter, the daughter of another
German who was a pawn in a scheme to smuggle unknown items of the collapsing Reich. The first twin they
discover—Hilde Monsalt, a woman who had lived a solitary life in a Jewish neighborhood of Boston—is already dead,
the victim of a grisly murder. Her stomach had been sliced open and an odd, smaller tear made in the area of her
appendix. It soon turns out that, not long before her death, Monsalt discovered that she was a beneficiary of a mysterious
will. The search then jumps the Atlantic to England, where Corvane, the powerful company funding Kettering’s research,
pushes Linwell, the bank that served as an executor for the will, to release information on another set of twins—who also
turn out to be dead. The novel’s settings are vivid and refreshingly detailed and include a grotesque concentration camp
in Jena, Germany, as well as the Arcadian French Riviera. The cast of villains is equally colorful, and the story takes
many unexpected turns. Kettering, on the other hand, is a stock protagonist about whom readers learn little more than his
hair color, his profession, and the fact that he enjoys sailing. Corvane, meanwhile, has the convenient ability to coerce
any organization or suspect, but it’s never treated with any scrutiny itself. The novel could also have used a stronger
copy edit; for example, various characters’ thoughts are rendered inconsistently, either in all-caps or underlined. Despite
these issues, however, the overall story is excellent and a reason to look forward to more from this author.
An often audacious Nazi mystery with plenty of well-placed plot twists.

FOR ALL DESIGNERS!!!!!!!!!below is the story of ASH LANTERN, ( THE LANTERN.)FOR THOSE DESIGNERS WHO COULD NOT OPEN THE FILE ON THE CONTEST PAGE.ASH LANTERN (THE LANTERN)Waldecott, RichardManuscriptBOOK REVIEWHirshhorn (A Choir of Tinkers, 1983, etc.) offers an animated chase through Boston and Europe as his characters unravela mystery involving six pairs of identical Jewish twins saved from a German concentration camp.In 1965, Simon Kettering, a scientist fruitlessly searching for the secret of telepathy, receives a tantalizing report ofmacabre experiments conducted by Oskar Veltmann, a Nazi researcher on a similar mission. Kettering searches for thetwins who were the subjects of Veltmann’s experiments, and he gets help from Greta Sauter, the daughter of anotherGerman who was a pawn in a scheme to smuggle unknown items of the collapsing Reich. The first twin theydiscover—Hilde Monsalt, a woman who had lived a solitary life in a Jewish neighborhood of Boston—is already dead,the victim of a grisly murder. Her stomach had been sliced open and an odd, smaller tear made in the area of herappendix. It soon turns out that, not long before her death, Monsalt discovered that she was a beneficiary of a mysteriouswill. The search then jumps the Atlantic to England, where Corvane, the powerful company funding Kettering’s research,pushes Linwell, the bank that served as an executor for the will, to release information on another set of twins—who alsoturn out to be dead. The novel’s settings are vivid and refreshingly detailed and include a grotesque concentration campin Jena, Germany, as well as the Arcadian French Riviera. The cast of villains is equally colorful, and the story takesmany unexpected turns. Kettering, on the other hand, is a stock protagonist about whom readers learn little more than hishair color, his profession, and the fact that he enjoys sailing. Corvane, meanwhile, has the convenient ability to coerceany organization or suspect, but it’s never treated with any scrutiny itself. The novel could also have used a strongercopy edit; for example, various characters’ thoughts are rendered inconsistently, either in all-caps or underlined. Despitethese issues, however, the overall story is excellent and a reason to look forward to more from this author.An often audacious Nazi mystery with plenty of well-placed plot twists. Added Tuesday, June 2, 2015

BUDGET NOW $700 !!!!!!! STORY DETAILS NOW UPLOADED TO THE BRIEF.

BUDGET OVER $700 !!!!!!!

adult; males; history buffs; world war II buffs; groups interested in mental telepathy;
people who want their money's worth ona challenging read; people who have faith in the Orvell Notices.

Sans Serif
• arial.

• front and back cover, spine. a design which grabs enough to want to read back text.
• design to emphasize the puzzle, labyrinth,, riddle, complexity, deceptions, twists, false leads,masquerades,double-dealing, trickiness of the plot.
• presence of identical twins; a treasure.
• the naivety of the american; the duplicities of the germans; the diabolical schemes of the germans. the vulnerability of the children. the ??? suspect mental capability of the identical twins.
• marching nazis,
• ? prominent swastika.
• no horror.
• no supernatural mumbo-jumbo.

```html
<!DOCTYPE html>
<html lang="en">
<head>
<meta charset="utf-8">
<title>Ash Lantern – Book Cover Spread</title>
<link rel="stylesheet" href="https://fonts.googleapis.com/css2?family=Oswald:wght@500;700&family=Arimo:wght@400;700&display=swap">
<style>
  :root {
    --page-bg: #e9e9e9;
    --cover-black: #0d0d0e;
    --cover-deep: #1b1c1f;
    --glow-gold: #d9a441;
    --type-white: #f4f4f2;
    --photo-grey: #8c8f94;
  }
  * { box-sizing: border-box; margin: 0; padding: 0; }
  html, body {
    width: 1200px; height: 900px; overflow: hidden;
    background: var(--page-bg);
  }
  .spread {
    position: absolute; left: 132px; top: 120px;
    width: 936px; height: 660px;
    display: flex;
    box-shadow: 0 10px 30px rgba(0,0,0,.25);
  }
  /* ---------- back cover ---------- */
  .back-cover {
    position: relative; width: 440px; height: 660px;
    background:
      radial-gradient(ellipse 70% 45% at 45% 30%, rgba(120,122,128,.35), transparent 70%),
      radial-gradient(ellipse 60% 40% at 60% 80%, rgba(90,92,98,.3), transparent 70%),
      linear-gradient(160deg, var(--cover-deep), var(--cover-black));
    color: var(--type-white);
    font-family: "Arimo", Arial, sans-serif;
  }
  .back-copy {
    position: absolute; left: 34px; top: 42px; width: 372px;
    font-size: 10.6px; line-height: 1.42;
  }
  .back-copy p { margin-bottom: 14px; }
  .author-bio {
    position: absolute; left: 34px; top: 488px; width: 372px;
    display: flex; gap: 14px; align-items: flex-start;
    font-size: 10.6px; line-height: 1.4;
  }
  .author-photo {
    flex: 0 0 40px; height: 44px;
    background: linear-gradient(180deg, #a9acb0, var(--photo-grey));
    border: 2px solid var(--type-white);
  }
  .barcode-space {
    position: absolute; right: 20px; bottom: 22px;
    width: 136px; height: 80px; background: #ffffff;
  }
  /* ---------- spine ---------- */
  .spine {
    position: relative; width: 56px; height: 660px;
    background: linear-gradient(90deg, #050506, #141416 50%, #050506);
    color: var(--type-white);
    font-family: "Oswald", "Arial Narrow", sans-serif;
  }
  .spine-title, .spine-author {
    position: absolute; left: 50%;
    writing-mode: vertical-rl;
    transform: translateX(-50%);
    letter-spacing: 4px; white-space: nowrap;
    font-weight: 500;
  }
  .spine-title { top: 40px; font-size: 17px; }
  .spine-author { bottom: 60px; font-size: 16px; font-weight: 700; }
  /* ---------- front cover ---------- */
  .front-cover {
    position: relative; width: 440px; height: 660px; overflow: hidden;
    background: var(--cover-black);
    color: var(--type-white);
    font-family: "Oswald", "Arial Narrow", sans-serif;
  }
  .cover-art {
    position: absolute; inset: 0;
    background:
      radial-gradient(circle at 48% 46%, rgba(255,226,150,.95) 0, var(--glow-gold) 5%, rgba(138,90,34,.55) 16%, transparent 34%),
      radial-gradient(ellipse 80% 60% at 50% 50%, rgba(74,76,80,.55), transparent 75%),
      linear-gradient(180deg, #1e1f22 0%, #2b2c30 45%, #0c0c0d 100%);
  }
  .review-quote {
    position: absolute; top: 22px; left: 10px; right: 10px;
    text-align: center; white-space: nowrap;
    font-family: "Arimo", Arial, sans-serif; font-weight: 700;
    font-size: 10.5px; line-height: 1.5;
  }
  .review-quote .source { display: block; padding-left: 40px; }
  .title {
    position: absolute; top: 92px;
    writing-mode: vertical-rl;
    font-weight: 700; font-size: 72px; line-height: 1;
    letter-spacing: 5px; white-space: nowrap;
  }
  .title-reversed { left: 42px; transform: rotate(180deg); }
  .title-main { left: 148px; }
  .author-name {
    position: absolute; left: 0; right: 0; bottom: 30px;
    text-align: center; white-space: nowrap;
    font-weight: 700; font-size: 44px; letter-spacing: 1px;
  }
</style>
</head>
<body>
  <main class="spread">
    <section class="back-cover">
      <div class="back-copy">
        <p>Lorem ipsum dolor sit amet, et prima altera inciderint pro, eam cu commodo sanctus nostrum. Etir facete nec id, vocent aliquando repudiandae vel ei. Has prima admodum te, vel cu simul impetus, ei qui inani vocibus. Ex eam pertinax atomorum antiopam, dolor graeco mnesarchum ius in. Ea vel singulis accusamus dissentiet.</p>
        <p>Mucius docendi ad vim. Mei ei laudem salutandi, labitur graecis salutandi at sit. Prima timeam urbanitas pri ea, nisl nemore ponderum ad sea. His at wisi munere quodsi, nibh ludus adversarium pro ea. His veri ubique impetus no, id possim corrumpit sed.</p>
        <p>Sea timeam definiebas no, vix eripuit complectitur ne. Antiopam qualisque splendide ex eam, duo no invidunt disputando. Sit no dico saperet persequeris. Voluptua vituperatoribus pro id, minim populo per in, his an eros nostrud fusset. Pro omnes fastidii eu.</p>
        <p>An est liber tritani, dico quas denique per eu. Stet porro impetus vix no. His prima ocurreret scriptorem ex, te dicat cotidieque mea. Case elaboraret reformidans no his, eu vix prima appareat erroribus, admodum salutatus nam id. Te vocent scripta nostrud vim, solum dissentet no has.</p>
        <p>An dicta eiure perpetua pro. Altera perfecto convenire ex per, at eum magna ornatus. Eu cum accusata contentiones consequuntur, ex quo tempor corpora delectus, vix ei velit euismod.</p>
      </div>
      <div class="author-bio">
        <div class="author-photo" role="img" aria-label="Small portrait photo of the author"></div>
        <p>Lorem ipsum dolor sit amet, et prima altera inciderint pro, eam cu commodo sanctus nostrum. Etir facete nec id, vocent aliquando repudiandae vel ei</p>
      </div>
      <div class="barcode-space" aria-label="Space reserved for ISBN"></div>
    </section>

    <section class="spine">
      <span class="spine-title">ASH LANTERN&nbsp;&nbsp;THE LANTERN</span>
      <span class="spine-author">WALDECOT</span>
    </section>

    <section class="front-cover">
      <div class="cover-art" role="img" aria-label="Overhead view of a dark stone labyrinth with a glowing lantern light and two distant figures at its centre"></div>
      <p class="review-quote">“AN ANIMATED CHASE…[WE] LOOK FORWARD TO MORE FROM THIS AUTHOR.”<span class="source">~ ORVELL</span></p>
      <h1>
        <span class="title title-reversed">ASH LANTERN</span>
        <span class="title title-main">THE LANTERN</span>
      </h1>
      <p class="author-name">LEONARD WALDECOT</p>
    </section>
  </main>
</body>
</html>
```